Choc biz start-up needs packaging design

We are a start-up chocolate company called 'Maison Verlaque Confections'. Our motto is 'Craft Beyond the Ordinary'. Themes associated with the company are: quality, social change, environmental awareness, innovation, refined and modern (with a strong emphasis on 'refined' - but not to the point of being boring!). Our product consists of bite-sized chocolate pieces. Being in the modern style, our products will utilise colour similar to www.tarvelbrookconfections.com, but with more restraint (that is, with a greater emphasis on the natural colours of chocolate: so the shades of white, milk and dark choc). We require a design for the exterior of both the LID and BASE.
More info:
---------------------------
Box shape and structure: See File 'cimg5416'
Logo: A logo has already been prepared, see 'AI-CMYK'. The main theme implied by this logo, is of 'nobility'. The style of lion itself is called a heraldic lion and traces back to European nobility. The colour of the logo is not fixed.
Product/Company info: See File 'back 3c', this text will need to go on the back of the box but how it appears is for you to decide
Dimensions (approx): note the length and width may vary but the height will stay at 33mm. This is because the design will be used for 9, 16 and 25 piece boxes.
Of entire box: 150mm x 150mm x 33mm high
Of lid: 150mm x 150mm x 23mm high (note this means that the base will be visible from the sides, when the box is closed)
Colours to avoid: large amounts of black and/or white
Colours to use: branding colours not yet determined so the designer is welcome to use any colours that s/he wishes.
File format: will require file to eventually be provided in vector format
Other: packaging will be CMYK printed and can be either matte/gloss laminated. To reduce costs, there will be no heat-stamping/embossing/etc.
Thoughts on other choc packaging:
File named '626808': Nice, but a little too plain and static (for what I'm after).
File named 'index3': Nice, but too traditional (for what I'm after).
File named 'imagesc': Nice, a little too modern and simple (for what I'm after). To me, it doesn't say refined enough.
File named '12cm cover colour a': This was the design that I'd been working on. But I'm not a graphic designer, it looks incomplete and I feel that it's incorporating elements potentially too ornate to incorporate into the overall company branding. I'm just as likely to choose an all-new design that I like than to pick one that improves upon what I'd started (assuming the issues I had with the design are also addressed).
Updates
For those who read the brief on the 6th of July, or earlier:
It's come to my attention that the file numbers referred to in the brief did not match the file numbers that I uploaded (PixelGuild somehow jumbled it all up). I've since edited the brief to make references to the file names and not numbers. My apologies for any confusion caused.
Industry/Entity Type
Chocolate Company
Look and feel
Each slider illustrates characteristics of the customer's brand and the style your logo design should communicate.

```html
<!DOCTYPE html>
<html lang="en">
<head>
<meta charset="utf-8">
<title>Maison Verlaque Confections – Lid Design</title>
<link rel="stylesheet" href="https://fonts.googleapis.com/css2?family=Cinzel:wght@400&display=swap">
<style>
  :root {
    --cocoa: #5a2b2b;
    --pistachio: #a6cd3d;
    --pistachio-soft: #9ec53a;
    --cream: #f1d3a9;
    --ink: #4a1f1f;
    --guide: rgba(190, 40, 50, 0.55);
    --page: #ffffff;
  }
  html, body {
    margin: 0;
    padding: 0;
    overflow: hidden;
    background: var(--page);
  }
  .canvas {
    position: relative;
    width: 882px;
    height: 1200px;
    background: var(--page);
    overflow: hidden;
  }
  .lid {
    position: absolute;
    left: 138px;
    top: 33px;
    width: 607px;
    height: 607px;
    background: var(--cocoa);
    overflow: hidden;
  }
  .lid__band {
    position: absolute;
    left: 0;
    top: 160px;
    width: 100%;
    height: 285px;
    background: var(--pistachio);
  }
  .lid__trim {
    position: absolute;
    left: 0;
    width: 100%;
  }
  .lid__trim--top { top: 134px; }
  .lid__trim--bottom { top: 445px; }
  .lid__pattern {
    position: absolute;
    left: 0;
    top: 232px;
    width: 100%;
    height: 130px;
    background: var(--pistachio-soft);
    opacity: 0.55;
  }
  .lid__flourish {
    position: absolute;
    left: 390px;
    top: 296px;
    width: 212px;
    height: 120px;
    border-radius: 60px 60px 60px 10px;
    background: linear-gradient(120deg,
      rgba(90, 43, 43, 0) 0%,
      rgba(90, 43, 43, 0.09) 100%);
  }
  .lid__guide {
    position: absolute;
    left: 70px;
    top: 71px;
    width: 465px;
    height: 466px;
    border: 1px solid var(--guide);
    box-sizing: border-box;
    opacity: 0.5;
  }
  .brand {
    position: absolute;
    left: 180px;
    top: 234px;
    width: 240px;
    text-align: center;
    color: var(--ink);
    font-family: "Cinzel", "Times New Roman", serif;
    font-weight: 400;
    line-height: 1;
  }
  .brand__mark {
    display: block;
    width: 44px;
    height: 44px;
    margin: 0 auto 14px;
    border-radius: 50%;
    background: var(--ink);
  }
  .brand__name {
    display: block;
    font-size: 16px;
    letter-spacing: 0.5px;
  }
  .brand__sub {
    display: block;
    margin-top: 3px;
    font-size: 7px;
    letter-spacing: 2px;
  }
  .tagline {
    position: absolute;
    left: 294px;
    top: 424px;
    margin: 0;
    color: var(--ink);
    font-family: "Cinzel", "Times New Roman", serif;
    font-weight: 400;
    font-size: 11px;
    letter-spacing: 0.3px;
    white-space: nowrap;
  }
</style>
</head>
<body>
<main class="canvas">
  <section class="lid" aria-label="Chocolate box lid design">
    <div class="lid__band"></div>

    <svg class="lid__trim lid__trim--top" width="607" height="26" viewBox="0 0 607 26" aria-hidden="true">
      <rect x="0" y="2" width="607" height="2" fill="var(--cream)"/>
      <rect x="0" y="9" width="607" height="5" fill="var(--cream)"/>
      <rect x="0" y="19" width="607" height="3" fill="var(--cream)"/>
    </svg>
    <svg class="lid__trim lid__trim--bottom" width="607" height="26" viewBox="0 0 607 26" aria-hidden="true">
      <rect x="0" y="4" width="607" height="3" fill="var(--cream)"/>
      <rect x="0" y="12" width="607" height="5" fill="var(--cream)"/>
      <rect x="0" y="22" width="607" height="2" fill="var(--cream)"/>
    </svg>

    <div class="lid__pattern" role="img" aria-label="Faint repeating flower motif across the green band"></div>
    <div class="lid__flourish" role="img" aria-label="Hand-drawn ribbon flourish in dark chocolate brown"></div>

    <div class="lid__guide" aria-hidden="true"></div>

    <div class="brand">
      <span class="brand__mark" aria-hidden="true"></span>
      <span class="brand__name">MAISON VERLAQUE</span>
      <span class="brand__sub">CONFECTIONS</span>
    </div>

    <p class="tagline">CRAFT BEYOND THE ORDINARY</p>
  </section>
</main>
</body>
</html>
```